Poster promoting the "Golden Crust Day"

The Meridan Federation of Oven Crafts (MFOC) created the "Golden Crust Day" in 2006. It is celebreated each year together with the GNX "Harvest Table Day" on 16th October.
After using different posters for a few years, MFOC decided to settle on a permanent poster some time ago, in order to allow people to recognize the poster long-term.
Now, MFOC feels that this permanent poster needs an update and modernization, apart from including the new MFOC logo.
Requisits:
1. Must include the new MFOC logo
2. The poster should reflect the importance of bread in the world and convey an image of health, innovation and tradition.
3. One version with text, one version without text
4. Text version: one poster for each of the four official MFOC languages:
ENGLISH: Golden Crust Day / 16th October
GERMAN: Goldkrustentag / 16. Oktober
SPANISH: Día de la Corteza Dorada / 16 de Octubre
FRENCH: Journée de la Croûte Dorée / 16 Octobre
5. Colours must be defined with RGB colour code.
MFOC will take a decision regarding the new poster design during the next meeting of its Marketing Commission on March 24th, 2015. Therefore, please submit your proposals by 18th March in order to allow for pre-selection and modification requests.
More about MFOC at www.meridanovencrafts.org.

```html
<!DOCTYPE html>
<html lang="en">
<head>
<meta charset="utf-8">
<title>Golden Crust Day – 16th October</title>
<link rel="stylesheet" href="https://fonts.googleapis.com/css2?family=Cinzel:wght@400;500&family=Syncopate:wght@700&family=Quicksand:wght@500&display=swap">
<style>
  :root {
    --paper: #fdf5e9;
    --crust-red: #7a1111;
    --continent-red: #741212;
    --wheat-orange: #f5a82a;
    --bread-gold: #e9a24a;
    --bread-light: #f3cf8c;
    --bread-brown: #b8622a;
    --logo-blue: #3f9ad6;
  }
  * { margin: 0; padding: 0; box-sizing: border-box; }
  html, body {
    width: 849px;
    height: 1200px;
    overflow: hidden;
    background: var(--paper);
  }
  .poster {
    position: relative;
    width: 849px;
    height: 1200px;
    background: var(--paper);
    color: var(--crust-red);
  }
  .brand {
    position: absolute;
    left: 42px;
    top: 62px;
    display: flex;
    align-items: center;
    gap: 12px;
  }
  .brand-name {
    font-family: "Cinzel", serif;
    font-weight: 500;
    font-size: 44px;
    letter-spacing: 2px;
    color: var(--crust-red);
    line-height: 1;
  }
  .brand-dot {
    width: 20px;
    height: 20px;
    border-radius: 50%;
    background: var(--logo-blue);
  }
  .bread-globe {
    position: absolute;
    left: 116px;
    top: 146px;
    width: 620px;
    height: 600px;
  }
  .title {
    position: absolute;
    left: 0;
    width: 849px;
    text-align: center;
    font-family: "Cinzel", serif;
    font-weight: 400;
    color: var(--crust-red);
    line-height: 1;
    white-space: nowrap;
  }
  .title-top {
    top: 824px;
    font-size: 64px;
    letter-spacing: 1px;
  }
  .title-main {
    top: 908px;
    font-size: 124px;
    letter-spacing: 4px;
  }
  .date-row {
    position: absolute;
    left: 150px;
    top: 1050px;
    width: 550px;
    display: flex;
    align-items: center;
    gap: 14px;
  }
  .date-bar {
    flex: 1;
    height: 10px;
    background: var(--wheat-orange);
  }
  .date {
    font-family: "Syncopate", sans-serif;
    font-weight: 700;
    font-size: 25px;
    color: var(--crust-red);
    white-space: nowrap;
    line-height: 1;
  }
  .date sup { font-size: 14px; vertical-align: 10px; }
  .site {
    position: absolute;
    left: 0;
    width: 849px;
    top: 1112px;
    text-align: center;
    font-family: "Quicksand", sans-serif;
    font-weight: 500;
    font-size: 22px;
    color: var(--crust-red);
    letter-spacing: 0.5px;
  }
</style>
</head>
<body>
  <main class="poster">
    <header class="brand">
      <span class="brand-name">MFOC</span>
      <span class="brand-dot"></span>
    </header>

    <svg class="bread-globe" viewBox="0 0 620 600" role="img" aria-label="Globe of the world: dark red continents, with the oceans filled by golden breads, bagels, baguettes, rolls and sliced loaves from around the world">
      <defs>
        <linearGradient id="breadGlobeFill" x1="0.85" y1="0.1" x2="0.2" y2="0.95">
          <stop offset="0%" stop-color="var(--continent-red)"/>
          <stop offset="38%" stop-color="var(--continent-red)"/>
          <stop offset="62%" stop-color="var(--bread-brown)"/>
          <stop offset="82%" stop-color="var(--bread-gold)"/>
          <stop offset="100%" stop-color="var(--bread-light)"/>
        </linearGradient>
      </defs>
      <ellipse cx="310" cy="300" rx="308" ry="298" fill="url(#breadGlobeFill)"/>
    </svg>

    <h1 class="title title-top">GOLDEN CRUST</h1>
    <p class="title title-main">DAY</p>

    <div class="date-row">
      <span class="date-bar"></span>
      <span class="date">16<sup>TH</sup> OCTOBER</span>
      <span class="date-bar"></span>
    </div>

    <p class="site">meridanovencrafts.org</p>
  </main>
</body>
</html>
```